Website needed for Entertainment Company [Wordpress & Mobile Site] (Contest)

"Vault Learning" does Acrobatic Educational Shows for schools.
We need a 4-Page Wordpress site, for BOTH Desktop & Mobile
THINGS WE'D LIKE ON THE HOME PAGE
- Book Now buttons
- Panel advertising "Kindness-First Tumbling Tour" with subheading "Educating the Victim, Empowering the Bystander, and Enlightening the Bully" with Photo & 'Read More'
- text somewhere saying "Vault Learning engages children in important topics, by utilising Parkour & Acrobatics to captivate and enthrall todays youngest generation."
- Panel advertising Teachers Resources: "Curriculum based resources for teachers including lesson plans, workbooks, and physical activities for before & after the show." Maybe even some boxes that say a subject that is covered (eg. Mathematics. Science. PD/H/PE.)
- Everything else that you recommend
4 PAGES:
- Home Page
- About Us
- Our Program & Shows
- Teachers Resources Portal
NOTE: Transparent & Source files for logo will be provided soon (recently finished being designed)

```html
<!DOCTYPE html>
<html lang="en">
<head>
<meta charset="utf-8">
<title>Vault Learning</title>
<link href="https://fonts.googleapis.com/css2?family=Montserrat:wght@400;500;600;700&display=swap" rel="stylesheet">
<style>
:root{
  --green:#23874f;
  --blue:#0565a8;
  --orange:#e8821e;
  --ink:#1b1b1b;
  --grey-text:#555;
  --header-bg:#e5e5e5;
  --footer-bg:#050505;
  --white:#fff;
}
*{box-sizing:border-box;margin:0;padding:0}
html,body{width:1200px;height:2750px;overflow:hidden}
body{position:relative;font-family:'Montserrat',sans-serif;background:var(--white);color:var(--ink)}
.abs{position:absolute}
.site-header{left:0;top:0;width:1200px;height:88px;background:var(--header-bg)}
.brand{display:flex;align-items:center;gap:10px;font-weight:700;color:var(--orange)}
.brand-mark{border-radius:50%;background:var(--orange)}
.site-header .brand{left:115px;top:22px;font-size:30px}
.site-header .brand-mark{width:36px;height:36px}
.main-nav{right:115px;top:34px;display:flex;gap:29px;font-size:14px;color:#555}
.hero-photo{left:0;top:88px;width:1200px;height:620px;background:linear-gradient(110deg,#b8c1ca 0%,#a9b3bd 35%,#c2a35a 55%,#b89a52 70%,#c6ccd3 100%)}
.shapes{left:0;top:0;width:1200px;height:2750px}
.hero-title{left:112px;top:228px;font-size:47px;font-weight:700;line-height:56px;color:var(--ink)}
.slider-dots{left:1130px;top:333px;width:20px}
.slider-dots span{position:absolute;left:50%;transform:translateX(-50%);border-radius:50%;background:var(--white)}
.section-title{left:0;width:1200px;text-align:center;font-weight:700;color:var(--green)}
.show-title{top:742px;font-size:40px}
.card{top:854px;height:361px;background:var(--white);box-shadow:0 4px 24px rgba(0,0,0,.1);text-align:center}
.card-photo{width:100%;height:172px}
.card h3{margin-top:29px;font-size:18px;font-weight:500;color:var(--green)}
.card p{margin:13px auto 0;width:235px;font-size:14px;line-height:23.5px;color:var(--grey-text)}
.card-arrow{position:absolute;left:50%;bottom:-26px;transform:translateX(-50%);width:53px;height:53px;border-radius:50%;background:var(--white);box-shadow:0 3px 12px rgba(0,0,0,.12);display:flex;align-items:center;justify-content:center}
.card-arrow.active{background:var(--green)}
.tagline{left:0;top:1410px;width:1200px;text-align:center;color:var(--white);font-size:21px;font-weight:500;line-height:34px}
.book-btn{left:501px;top:1500px;width:203px;height:59px;border:2px solid var(--white);border-radius:30px;color:var(--white);font-size:20px;font-weight:500;display:flex;align-items:center;justify-content:center}
.res-title{top:1720px;font-size:47px;font-weight:600}
.res-sub{left:0;top:1792px;width:1200px;text-align:center;font-size:19px;color:var(--grey-text)}
.res-line{left:228px;top:1975px;height:180px;border-left:1px dashed var(--orange)}
.res-item{left:187px;display:flex;align-items:center;gap:27px;font-size:21px;font-weight:500}
.res-icon{width:82px;height:82px;border-radius:50%;display:flex;align-items:center;justify-content:center}
.res-dots span{position:absolute;top:2277px;width:12px;height:12px;border-radius:50%}
.video-photo{left:567px;top:1879px;width:521px;height:337px;background:linear-gradient(160deg,#7d8596,#5b6170 60%,#3a3d46)}
.play{left:786px;top:2007px;width:84px;height:84px;border-radius:50%;background:var(--orange);display:flex;align-items:center;justify-content:center}
.footer-brand{left:137px;top:2500px;font-size:34px}
.footer-brand .brand-mark{width:40px;height:40px}
.social span{position:absolute;top:2600px;width:24px;height:24px;border-radius:50%;border:1.5px solid var(--white)}
.footer-col{color:var(--white)}
.footer-col h4{font-size:21px;font-weight:500;margin-bottom:18px}
.footer-col ul{list-style:none;font-size:13.5px;font-weight:500}
.footer-col li{height:30px}
.contact-list{font-size:13.5px;line-height:21.5px}
.copyright{left:0;top:2704px;width:1200px;text-align:center;color:var(--white);font-size:14.5px;font-weight:500}
</style>
</head>
<body>

<header class="site-header abs">
  <div class="brand abs"><span class="brand-mark"></span>Vault Learning</div>
  <nav class="main-nav abs"><span>Home</span><span>About Us</span><span>Program &amp; Shows</span><span>Teachers Resources Portal</span><span>Contact Us</span></nav>
</header>

<div class="hero-photo abs" role="img" aria-label="Group of acrobats in mustard leotards leaping in formation against a grey studio backdrop"></div>

<svg class="shapes abs" viewBox="0 0 1124 2576" preserveAspectRatio="none" aria-hidden="true">
  <polygon points="605,560 1124,467 1124,628" fill="#0565a8"/>
  <polygon points="0,663 605,560 1124,628 1124,700 0,700" fill="#fff"/>
  <polygon points="0,1222 1124,1295 1124,1565 0,1485" fill="#23874f"/>
  <polygon points="0,2215 240,2238 0,2275" fill="#0565a8"/>
  <polygon points="840,2148 1124,2108 1124,2215" fill="#0565a8"/>
  <polygon points="0,2275 240,2238 840,2148 1124,2215 1124,2576 0,2576" fill="#050505"/>
</svg>

<h1 class="hero-title abs">Welcome To<br>Vault Learning</h1>
<div class="slider-dots abs">
  <span style="top:0;width:20px;height:20px;border:3px solid #fff;background:transparent"></span>
  <span style="top:5px;width:10px;height:10px"></span>
  <span style="top:30px;width:10px;height:10px"></span>
  <span style="top:51px;width:10px;height:10px"></span>
</div>

<h2 class="section-title show-title abs">Kindness-First Tumbling Tour</h2>

<article class="card abs" style="left:153px;width:282px">
  <div class="card-photo" role="img" aria-label="Child climbing a rope net in a forest playground" style="background:linear-gradient(160deg,#6f7a52,#9a8a6a 60%,#b4a48a)"></div>
  <h3>Educating The Victim</h3>
  <p>Lorem ipsum dolor sit amet, consectetur adipiscing elit, sed do eiusmod tempor</p>
  <span class="card-arrow"><svg width="22" height="22" viewBox="0 0 22 22"><path d="M3 11h15M12 5l6 6-6 6" stroke="#444" stroke-width="2.4" fill="none"/></svg></span>
</article>
<article class="card abs" style="left:459px;width:282px">
  <div class="card-photo" role="img" aria-label="Two dancers in yellow performing a duet against a bright blue backdrop" style="background:linear-gradient(160deg,#2bb4e0,#1f9cd0)"></div>
  <h3>Empowering the Bystander</h3>
  <p>Lorem ipsum dolor sit amet, consectetur adipiscing elit, sed do eiusmod tempor</p>
  <span class="card-arrow active"><svg width="22" height="22" viewBox="0 0 22 22"><path d="M3 11h15M12 5l6 6-6 6" stroke="#fff" stroke-width="2.4" fill="none"/></svg></span>
</article>
<article class="card abs" style="left:770px;width:282px">
  <div class="card-photo" role="img" aria-label="Dancer balancing in an arabesque in a bright studio" style="background:linear-gradient(160deg,#d9d9d6,#c4c3bd 60%,#eeeeea)"></div>
  <h3>Enlightening the Bully</h3>
  <p>Lorem ipsum dolor sit amet, consectetur adipiscing elit, sed do eiusmod tempor</p>
  <span class="card-arrow"><svg width="22" height="22" viewBox="0 0 22 22"><path d="M3 11h15M12 5l6 6-6 6" stroke="#444" stroke-width="2.4" fill="none"/></svg></span>
</article>

<p class="tagline abs">"Vault Learning engages children in important topics, by utilising<br>Parkour &amp; Acrobatics to captivate and enthrall todays youngest generation."</p>
<div class="book-btn abs">Book Now</div>

<h2 class="section-title res-title abs">Teachers Resources</h2>
<p class="res-sub abs">Curriculum based resources for teachers</p>

<div class="res-line abs"></div>
<div class="res-item abs" style="top:1894px;color:var(--orange)">
  <span class="res-icon" style="background:var(--orange)"><svg width="42" height="42" viewBox="0 0 42 42" fill="none" stroke="#fff" stroke-width="1.8"><rect x="16" y="6" width="20" height="14"/><path d="M20 13l3 3 6-6"/><circle cx="10" cy="12" r="3"/><path d="M10 16v12M6 28h30"/><circle cx="16" cy="33" r="2.5"/><circle cx="24" cy="33" r="2.5"/><circle cx="32" cy="33" r="2.5"/></svg></span>Lesson Plans
</div>
<div class="res-item abs" style="top:2025px;color:var(--green)">
  <span class="res-icon" style="background:var(--green)"><svg width="42" height="42" viewBox="0 0 42 42" fill="none" stroke="#fff" stroke-width="2"><path d="M8 12l14-5 14 5-14 5z"/><path d="M8 19l14 5 14-5M8 26l14 5 14-5"/></svg></span>Workbooks
</div>
<div class="res-item abs" style="top:2153px;color:var(--blue)">
  <span class="res-icon" style="background:var(--blue)"><svg width="42" height="42" viewBox="0 0 42 42" fill="none" stroke="#fff" stroke-width="2"><path d="M4 16l17-8 17 8-17 8z"/><path d="M12 20v8c0 3 18 3 18 0v-8M36 17v10"/></svg></span>Physical Activities
</div>
<div class="res-dots">
  <span style="left:213px;background:var(--blue)"></span>
  <span style="left:233px;background:#c8c8c8"></span>
</div>

<div class="video-photo abs" role="img" aria-label="Dance troupe in black leotards posing together in a studio"></div>
<div class="play abs"><svg width="50" height="50" viewBox="0 0 50 50" fill="none" stroke="#fff" stroke-width="2"><circle cx="25" cy="25" r="22"/><path d="M20 15l14 10-14 10z"/></svg></div>

<div class="brand footer-brand abs"><span class="brand-mark"></span>Vault Learning</div>
<div class="social">
  <span style="left:211px"></span><span style="left:247px"></span><span style="left:284px"></span><span style="left:319px"></span>
</div>

<div class="footer-col abs" style="left:522px;top:2440px">
  <h4>Information</h4>
  <ul><li>Home</li><li>About Us</li><li>Program &amp; Shows</li><li>Teachers Resources Portal</li><li>Contact Us</li></ul>
</div>
<div class="footer-col abs" style="left:816px;top:2440px">
  <h4>Contact Us</h4>
  <div class="contact-list">
    <p>Address:&nbsp; #10.Sed ut<br>perspiciatis unde omnis iste<br>Brookfield</p>
    <p style="margin-top:16px">Phone:&nbsp; 555 014 3210</p>
    <p style="margin-top:18px">Email:&nbsp; info@vaultlearning.com</p>
  </div>
</div>

<p class="copyright abs">© 2018 Copyrights | All Rights Reserved</p>

</body>
</html>
```